C U B A N - C I G A R S - F L Y E R

I need a double-sided 5x7 club type flyer for a Memorial Day Weekend Trip.
The main side design needs to be similar to the attached flyer example. The front design of flyer is KEY. The design will be awarded to the closest finished submission to the example flyer.
Both sides of the flyer should also included event and business logo, which are also attached. Both logos can be altered to fit printing need accordingly.
Front side content is also attached.
The back side design will be very simple. Consists of 3 travel images and trip description, and my contact very details. Same color design as front. The attached word document contains backside details for REFERENCE ONLY. Please focus on front side when submitting a design for this project.
Target Market(s)
A F R I C A N - A M E R I C A N - C I G A R - S M O K E R S
Industry/Entity Type
Travel Industry
Requirements
Must have
- All the elements of the attached information
Nice to have
- Masculine Images
Should not have
- Large Cigar focus to catch customer's attention

```html
<!DOCTYPE html>
<html lang="en">
<head>
<meta charset="utf-8">
<title>Cuba Cigar Gentlemen's Memorial Day Weekend Flyer</title>
<link href="https://fonts.googleapis.com/css2?family=Oswald:wght@500;600;700&family=Roboto+Condensed:ital,wght@0,400;0,700;1,700&family=Roboto:ital,wght@0,400;0,700;1,700&display=swap" rel="stylesheet">
<style>
  :root{
    --stage:#2b211b;
    --navy:#2a3f8f;
    --red:#d12a2e;
    --deep-red:#c9252a;
    --pink-top:#fbe9e9;
    --pink-bottom:#f3a6a8;
    --seal-fill:#f3c9cc;
    --band-pink:#f4a5a6;
    --ink:#111;
    --white:#fff;
    --photo-dark:#1f2128;
  }
  *{box-sizing:border-box;margin:0;padding:0}
  html,body{width:1200px;height:1200px;overflow:hidden;background:var(--stage)}
  .stage{position:relative;width:1200px;height:1200px}

  /* FRONT */
  .front{position:absolute;left:58px;top:63px;width:712px;height:515px;overflow:hidden;background:var(--photo-dark)}
  .front-photo{position:absolute;left:0;top:0;width:418px;height:515px;
    background:radial-gradient(ellipse at 25% 45%,#c98a2a 0,#6b4a25 22%,transparent 45%),
               radial-gradient(ellipse at 55% 85%,#8e1c22 0,#4a1418 30%,transparent 55%),
               linear-gradient(160deg,#5a6a4a 0,#3a3e44 40%,#23252c 100%)}
  .front-strip{position:absolute;right:0;top:0;width:67px;height:515px;
    background:linear-gradient(180deg,#3b4150 0,#2b2a2a 55%,#1a1c22 100%)}
  .brand{position:absolute;left:28px;top:385px;width:94px;height:94px;border:1.5px solid var(--white);border-radius:50%;
    display:flex;align-items:center;justify-content:center;text-align:center;
    font-family:"Roboto",sans-serif;font-weight:400;font-size:12px;letter-spacing:1px;color:var(--white);line-height:1.3}
  .panel{position:absolute;left:418px;top:0;width:227px;height:515px;
    background:linear-gradient(180deg,var(--pink-top) 0,#f7d0d1 45%,var(--pink-bottom) 100%);text-align:center}
  .kicker{margin-top:40px;font-family:"Roboto",sans-serif;font-weight:700;font-size:14px;color:var(--navy);line-height:1.2}
  .occasion{margin-top:2px;font-family:"Oswald",sans-serif;font-weight:600;font-size:19px;color:var(--navy);line-height:1.25}
  .year{font-family:"Oswald",sans-serif;font-weight:600;font-size:24px;color:var(--navy);line-height:1.1}
  .headline{margin-top:8px;font-family:"Oswald",sans-serif;font-weight:700;font-size:32px;line-height:1.08;color:var(--red);letter-spacing:.3px}
  .event-mark{position:relative;width:178px;height:178px;margin:14px auto 0;border:3px solid var(--navy);border-radius:50%;background:var(--seal-fill);
    display:flex;align-items:center;justify-content:center}
  .event-name{font-family:"Oswald",sans-serif;font-weight:600;font-size:24px;line-height:1.15;color:var(--navy)}
  .lead{margin-top:10px;font-family:"Roboto Condensed",sans-serif;font-weight:700;font-size:13px;line-height:1.4;color:var(--ink)}
  .cta{position:absolute;left:0;bottom:0;width:227px;height:92px;background:var(--deep-red);color:var(--white)}
  .cta-row{display:flex;align-items:center;justify-content:center;gap:6px;margin-top:6px}
  .book{font-family:"Oswald",sans-serif;font-weight:600;font-size:24px;line-height:1}
  .limited{background:#111;border-radius:12px;padding:2px 10px;font-family:"Roboto Condensed",sans-serif;font-weight:700;font-size:9px;line-height:1.05}
  .url{font-family:"Roboto Condensed",sans-serif;font-size:11.5px;margin-top:3px}
  .phone{font-family:"Oswald",sans-serif;font-weight:600;font-size:30px;line-height:1.1}

  /* BACK */
  .back{position:absolute;left:414px;top:620px;width:712px;height:514px;background:var(--white)}
  .gallery{position:absolute;left:27px;top:26px;width:658px;height:147px;border:1.5px solid #111;display:flex}
  .gallery > div{height:100%}
  .photo-cars{width:198px;background:linear-gradient(160deg,#d9c22a 0,#e04a8a 30%,#1e6fc4 65%,#6b7a8a 100%)}
  .map{width:228px;background:linear-gradient(180deg,#f4f7fb 0,#e3ecf5 55%,#f3b12f 80%,#eef3f8 100%)}
  .photo-cigars{width:232px;background:linear-gradient(150deg,#b57a4a 0,#6b3a1c 50%,#3a1e10 100%)}
  .story{position:absolute;left:32px;top:180px;width:647px;font-family:"Roboto Condensed",sans-serif;font-size:11.4px;line-height:13.6px;text-align:justify;color:var(--ink)}
  .band{position:absolute;left:29px;top:306px;width:655px;height:154px;background:var(--band-pink);font-family:"Roboto",sans-serif;color:var(--ink)}
  .chev{position:absolute;top:8px}
  .col-price{position:absolute;left:16px;top:8px;width:180px}
  .price{font-family:"Roboto",sans-serif;font-weight:700;font-size:16.5px;line-height:20px}
  .terms{font-weight:700;font-size:11.5px;line-height:14.5px}
  .fine{font-size:9.5px;line-height:12px;margin-top:10px}
  .col-incl{position:absolute;left:222px;top:3px;width:270px;font-size:11.5px;line-height:14.7px}
  .col-incl h3{font-weight:400;font-size:18px;line-height:20px}
  .col-incl .meals{font-weight:700;font-style:italic}
  .col-incl small{font-size:8.5px;font-weight:700;display:block;line-height:11px}
  .col-due{position:absolute;right:15px;top:14px;width:170px;text-align:right}
  .due{font-family:"Roboto Condensed",sans-serif;font-weight:700;font-size:17px;line-height:21px}
  .back-footer{position:absolute;left:0;top:468px;width:712px;text-align:center;font-family:"Roboto",sans-serif;font-weight:700;font-style:italic;font-size:15.5px}
</style>
</head>
<body>
<main class="stage">

  <section class="front">
    <div class="front-photo" role="img" aria-label="Photo of a glass of rum on ice, a smoking cigar and a red classic American car"></div>
    <div class="front-strip" role="img" aria-label="Photo continuation showing cigar smoke and a dark classic car"></div>
    <div class="brand">HARBOR<br>TRAVEL CO</div>

    <div class="panel">
      <p class="kicker">A Cuba Cigar Gentlemen's</p>
      <p class="occasion">MEMORIAL DAY WEEKEND</p>
      <p class="year">2018</p>
      <h1 class="headline">CIGARS, RUM &amp;<br>CLASSIC CARS...</h1>
      <div class="event-mark">
        <span class="event-name">PALM COAST<br>ESCAPES</span>
      </div>
      <p class="lead">Legally travel to cuba ad return<br>with real CUBAN CIGARS!</p>
      <div class="cta">
        <div class="cta-row"><span class="book">BOOK NOW</span><span class="limited">SPACE IS<br>LIMITED</span></div>
        <p class="url">www.coralroutetrips.com/CUBA2018</p>
        <p class="phone">123 456 7890</p>
      </div>
    </div>
  </section>

  <section class="back">
    <div class="gallery">
      <div class="photo-cars" role="img" aria-label="Photo of colorful classic cars parked in a row"></div>
      <div class="map" role="img" aria-label="Map of the flight route from Miami to Havana, Cuba"></div>
      <div class="photo-cigars" role="img" aria-label="Photo of a row of fine cigars"></div>
    </div>

    <p class="story">Cuba is the ultimate bucket list destination for any cigar lover. Now is your opportunity to legally travel to Cuba and experience a country that has been off limits to Americans for more than 50 years befor it changes. Smoke fine Cuban cigars, meet its resillent people and experience Cuba's fascinating culture. Tour cigar factories, watch expert cigar rollers, visit a humidor factory and workshop, tour the Old Harbor Rum Museum to learn firsthand the process of making rum followed by rum tasting and pairings with Cuban cigars in a private setting and much more, Explore the Pinar Del Rio located in the Vinales Valley konwn for its stunning ladnscapes and tobacco plantations. Visit the world famous Valdés Tobacco Plantation to see first hand where and how the tobacco process is grown for fine Cuban Cigars. The bucket list trip of a lifetime awaits on this people to people Cigar Journey to Cuba to learn first hand about Cuban cigars, meet the Cuban people, experience incredible cuisine, drivein classic American cars along the Malecon and experience the Cuban cigar process from <b><i>'seed to smoke'</i></b> and an opportunit to smoke in the birthplace of cirars!</p>

    <div class="band">
      <div class="col-price">
        <p class="price">Trip Cost : $2050<br>Deposit &nbsp;&nbsp;: $300</p>
        <p class="terms">Payment plans available<br>$300 Deposit Required<br>Final payment<br>Due By April 10, 2018</p>
        <p class="fine">*NON-REFUNDABLE<br>*Passport Required</p>
      </div>
      <svg class="chev" style="left:158px" width="50" height="140" viewBox="0 0 50 140"><path d="M6 4 L44 70 L6 136" fill="none" stroke="#444" stroke-width="3"/></svg>
      <div class="col-incl">
        <h3>4 Days / 3 Nights</h3>
        <p>5 Star Hotel Accommodations Based on<br>Double Occupancy<br>Roundtrip Coastline Airways Tickets from Fort<br>Lauderdale Florida - Cuba<br>Tour Bus Chauffeured Transportation<br>All Rum and Cigar Tour Events</p>
        <p class="meals">Select Meals</p>
        <small>(Breakfast, Welcome and Farewell Dinner)<br>and More!</small>
      </div>
      <svg class="chev" style="left:450px" width="50" height="140" viewBox="0 0 50 140"><path d="M6 4 L44 70 L6 136" fill="none" stroke="#444" stroke-width="3"/></svg>
      <div class="col-due">
        <p class="due">$300 Deposit<br>Required<br>Final payment Due<br>By April 10, 2018</p>
        <p class="fine" style="margin-top:24px">*NON-REFUNDABLE<br>*Passport Required</p>
      </div>
    </div>

    <p class="back-footer">For More Information Call: XXX-XXX-XXXX</p>
  </section>

</main>
</body>
</html>
```